New Architectural Firm Business Cards

New Business card to compliment previous pixel forum logo (attached). Please design a business card that is simple, modern, creative....please do not use "symbols", simply the logo and associated graphics/text. The front should contain name/address/phone/email/web address (with graphics).....back should be 100% graphic design using the logo somehow. Hoping for a two color (black and yellow) design. full bleed design, no borders

Target Market(s)

Commercial Architecture Clients

Industry/Entity Type

Architecture

Contact Information for Business Card

Please design a business card that is simple, modern, creative....please do not use "symbols", simply the logo and associated graphics/text. The front should contain name/address/phone/email/web address (with graphics).....back should be 100% graphic design using the logo somehow

Font styles to use
Sans Serif

Colors
FFF300
FFF600
FEFA6F
FFFEC7
FFFEE8

Requirements
Must have
• Clean, Modern Design
Should not have
• Stock images or "icons"

```html
<!DOCTYPE html>
<html lang="en">
<head>
<meta charset="utf-8">
<title>pixel forum – Business Card</title>
<link rel="stylesheet" href="https://fonts.googleapis.com/css2?family=Libre+Franklin:wght@400;700;800&family=Arimo:ital,wght@0,400;1,400&display=swap">
<style>
  :root {
    --backdrop: #6d6d6d;
    --card-black: #111111;
    --pattern-dark: #1c1c1c;
    --pattern-light: #2a2a2a;
    --brand-yellow: #f6c515;
    --ink-white: #ffffff;
  }
  html, body {
    margin: 0;
    padding: 0;
    width: 1200px;
    height: 1200px;
    overflow: hidden;
    background: var(--backdrop);
  }
  .canvas {
    position: relative;
    width: 1200px;
    height: 1200px;
  }
  .card {
    position: absolute;
    left: 250px;
    width: 700px;
    height: 400px;
    background: var(--card-black);
    overflow: hidden;
    box-shadow: 0 6px 18px rgba(0,0,0,0.35);
  }
  .card--back { top: 170px; }
  .card--front { top: 630px; }

  .back-pattern {
    position: absolute;
    inset: 0;
    background: linear-gradient(135deg, var(--pattern-dark), var(--pattern-light) 50%, var(--pattern-dark));
  }
  .back-brand {
    position: absolute;
    left: 50%;
    top: 50%;
    transform: translate(-50%, -50%);
    display: flex;
    align-items: center;
    gap: 14px;
  }
  .back-brand__square {
    width: 26px;
    height: 26px;
    background: var(--brand-yellow);
  }
  .back-brand__name {
    font-family: "Libre Franklin", sans-serif;
    font-weight: 800;
    font-size: 54px;
    color: var(--brand-yellow);
    letter-spacing: -1px;
  }

  .contact {
    position: absolute;
    left: 46px;
    top: 40px;
    font-family: "Arimo", sans-serif;
    color: var(--ink-white);
  }
  .contact__name {
    margin: 0;
    font-family: "Libre Franklin", sans-serif;
    font-weight: 800;
    font-size: 24px;
    letter-spacing: 0.5px;
    text-transform: uppercase;
    color: var(--brand-yellow);
  }
  .contact__title {
    margin: 2px 0 0;
    font-size: 15px;
  }
  .contact__rule {
    width: 18px;
    height: 2px;
    background: var(--brand-yellow);
    margin: 10px 0 12px;
  }
  .contact__lines {
    margin: 0;
    font-size: 15px;
    line-height: 1.45;
    font-style: normal;
  }

  .front-brand {
    position: absolute;
    right: -20px;
    bottom: -38px;
    font-family: "Libre Franklin", sans-serif;
    font-weight: 800;
    font-size: 150px;
    line-height: 1;
    letter-spacing: -6px;
    color: var(--brand-yellow);
    white-space: nowrap;
  }
</style>
</head>
<body>
<main class="canvas">
  <section class="card card--back" aria-label="Card back">
    <div class="back-pattern" role="img" aria-label="Tone-on-tone repeating pattern of the firm mark in dark grey"></div>
    <div class="back-brand">
      <span class="back-brand__square"></span>
      <span class="back-brand__name">pixel forum</span>
    </div>
  </section>

  <section class="card card--front" aria-label="Card front">
    <div class="contact">
      <h1 class="contact__name">Dana Whitcombe</h1>
      <p class="contact__title">President</p>
      <div class="contact__rule"></div>
      <p class="contact__lines">555 010 2288<br>hello@pixelforum.example<br>www.pixelforum.example</p>
      <div class="contact__rule"></div>
      <address class="contact__lines">48 Alder Grove Parkway<br>Suite 210, Easton</address>
    </div>
    <div class="front-brand">pixel forum</div>
  </section>
</main>
</body>
</html>
```